Brisbane IT support business needs our first letterhead (Contest)

Hello we are a Brisbane based Information Technology company providing support and services to small and medium sized businesses. We provide a range of services and solutions.

The business name is Kestrel Data Network Systems, or KDNS for short.

I am looking for a letterhead that looks professional (don't we all want that), but most importantly, it most utilize the colours in the logo attached, and any text used preferably in font type: HandelGotDBol.

```html
<!DOCTYPE html>
<html lang="en">
<head>
<meta charset="utf-8">
<title>Kestrel Data Network Systems — Letterhead</title>
<link rel="stylesheet" href="https://fonts.googleapis.com/css2?family=Michroma&family=Open+Sans:wght@400&display=swap">
<style>
  :root {
    --navy: #0f4766;
    --orange: #e2771f;
    --ink: #2b2b2b;
    --paper: #ffffff;
    --backdrop: #ececec;
    --watermark: #e6e6e6;
  }
  * { margin: 0; padding: 0; box-sizing: border-box; }
  html, body { width: 1200px; height: 1192px; overflow: hidden; background: var(--backdrop); }
  .letterhead {
    position: absolute; left: 220px; top: 58px;
    width: 760px; height: 1076px;
    background: var(--paper);
    box-shadow: 0 4px 18px rgba(0,0,0,0.08);
    overflow: hidden;
  }
  .brand {
    position: absolute; right: 48px; top: 64px;
    font-family: "Michroma", sans-serif; font-size: 13px; line-height: 1.3;
    color: var(--navy); text-transform: uppercase; letter-spacing: 0.5px;
    text-align: right;
  }
  .watermark {
    position: absolute; left: 200px; top: 330px;
    width: 360px; height: 360px; border-radius: 50%;
    background: var(--watermark);
  }
  .footer-bands { position: absolute; left: 0; top: 0; width: 760px; height: 1076px; }
  .contact {
    position: absolute; right: 40px; top: 900px;
    display: flex; gap: 10px; align-items: flex-end;
  }
  .contact-text { text-align: right; }
  .contact-name {
    font-family: "Michroma", sans-serif; font-size: 12px; line-height: 1.2;
    color: var(--navy); text-transform: uppercase; margin-bottom: 6px;
  }
  .contact-line {
    font-family: "Open Sans", sans-serif; font-size: 10px; line-height: 1.55;
    color: var(--ink); display: flex; justify-content: flex-end; align-items: center; gap: 6px;
  }
  .contact-line svg { width: 9px; height: 9px; fill: var(--navy); }
  .contact-rule { width: 1.5px; height: 58px; background: var(--orange); }
</style>
</head>
<body>
  <main class="letterhead">
    <header class="brand">Kestrel Data Network Systems</header>

    <div class="watermark" role="img" aria-label="Faint brand emblem watermark"></div>

    <section class="contact">
      <div class="contact-text">
        <div class="contact-name">Kestrel Data Network<br>Systems</div>
        <div class="contact-line">Your Commercial or office address
          <svg viewBox="0 0 10 10"><path d="M5 0a3.5 3.5 0 0 1 3.5 3.5C8.5 6 5 10 5 10S1.5 6 1.5 3.5A3.5 3.5 0 0 1 5 0zm0 2a1.5 1.5 0 1 0 0 3 1.5 1.5 0 0 0 0-3z"/></svg></div>
        <div class="contact-line">00.00.00.0000 &nbsp; 00.00.00.0000
          <svg viewBox="0 0 10 10"><path d="M2 0h2l1 3-1.5 1a6 6 0 0 0 2.5 2.5L7 5l3 1v2c0 1-1 2-2 2C4 10 0 6 0 2 0 1 1 0 2 0z"/></svg></div>
        <div class="contact-line">yourname@yourwebsite.com
          <svg viewBox="0 0 10 10"><path d="M0 2h10v6H0zM0 2l5 3.5L10 2v1L5 6.5 0 3z"/></svg></div>
        <div class="contact-line">www.yourwebsite.com
          <svg viewBox="0 0 10 10"><circle cx="5" cy="5" r="4.5" fill="none" stroke="#0f4766" stroke-width="1"/><path d="M0.5 5h9M5 0.5v9" stroke="#0f4766" stroke-width="0.8"/></svg></div>
      </div>
      <span class="contact-rule"></span>
    </section>

    <svg class="footer-bands" viewBox="0 0 760 1076" aria-hidden="true">
      <polygon points="0,1022 172,1022 196,1040 0,1040" fill="var(--navy)"/>
      <polygon points="184,1034 198,1034 226,1056 760,1056 760,1066 212,1066" fill="var(--orange)"/>
    </svg>
  </main>
</body>
</html>
```